wardrobe/costume stylist needs good business card for own business

Hi:)

I'm wanting a business card for my company. I am a freelance stylist.

I do wardrobe/costume stylist to TV commercials; Films; Fashion and Lifestyle shoots.

I'd like a design based around my name Rosalind Pember written nicely, maybe a colour? Up to you?!

I've attached a couple of images of business cards I like
.... be creative and have fun!

Thank you :)
Updates

Reason: I was trying to get my new business card ready for before I headed overseas Friday morning but I don't think that was realistic so I'd like to extend the deadline to give time to the project. Thank you

Hi designers:) Thank you for all your designs, I've extended the deadline until Sunday, so there's a bit more time. I've attached 3 pictures of business cards which I quite like, please take a look to see if it can be of help in your process. I like the pale plain or patterned background with dark font and the dark plain or patterned background with the pale font the motifs the feminine fonts the plain fonts I like the idea of playing with a circle or some shape on one side of the card with my name or initials as in the picture I have on my post could you play around with this idea a bit please? Thank you all for the work you've done :) Rosa

Hi I am working overseas til Saturday night sorry for no feedback until I teturn Thanks :) Rosa

Hi designers, Thank you all so much for submitting your designs, I really appreciate your input into my project :) I'm sorry I didn't get to respond to some comments, and give feedback. I didn't back from being away until later than I expected, and the deadline had passed then, so apologies. Thanks to you all again for all your really good designs :) Rosa

Target Market(s)

I am a freelance stylist my target audience is producers, production companies, photographers, directors...

Industry/Entity Type

Business

Requirements
Must have
• Rosalind Pember
Stylist or Wardrobe Stylist

email rosapember@quillnet.co.nz
Mobile 0218846193

(Don't have to use the words 'email' and 'mobile')
Nice to have
• Would like it to be double sided
Like B & W
Like pale colour background with dark font or white font
Like dark colour background with pale font
Should not have
• I would prefer it not to incorporate pictures

```html
<!DOCTYPE html>
<html lang="en">
<head>
<meta charset="utf-8">
<title>Rosalind Pember — Stylist business card</title>
<link href="https://fonts.googleapis.com/css2?family=Special+Elite&display=swap" rel="stylesheet">
<style>
  :root {
    --backdrop: #d9d2cc;
    --ink: #25273b;
    --paper: #f1efe2;
    --shadow: rgba(40, 30, 30, 0.18);
  }
  * { margin: 0; padding: 0; box-sizing: border-box; }
  html, body {
    width: 800px;
    height: 1200px;
    overflow: hidden;
    background: var(--backdrop);
    font-family: "Special Elite", "Courier New", monospace;
  }
  .canvas {
    position: relative;
    width: 800px;
    height: 1200px;
  }
  .card {
    position: absolute;
    left: 100px;
    width: 600px;
    height: 343px;
    overflow: hidden;
    box-shadow: 0 10px 24px var(--shadow);
  }
  .card--front { top: 170px; background: var(--ink); color: var(--paper); }
  .card--back  { top: 680px; background: var(--paper); color: var(--ink); }

  .name-disc {
    position: absolute;
    border-radius: 50%;
    display: flex;
    flex-direction: column;
    align-items: center;
    justify-content: center;
    text-align: center;
  }
  .card--front .name-disc {
    left: 250px; top: 16px;
    width: 310px; height: 310px;
    border: 4px solid var(--paper);
  }
  .card--back .name-disc {
    left: 222px; top: 93px;
    width: 156px; height: 156px;
    border: 3px solid var(--ink);
  }

  .name {
    line-height: 1.1;
    letter-spacing: 0.5px;
  }
  .card--front .name { font-size: 44px; }
  .card--back .name  { font-size: 21px; }

  .role { letter-spacing: 1px; }
  .card--front .role { font-size: 17px; margin-top: 18px; }
  .card--back .role  { font-size: 10px; margin-top: 8px; }

  .contact {
    position: absolute;
    left: 20px;
    bottom: 24px;
    font-size: 12px;
    font-style: normal;
    line-height: 1.3;
    text-align: center;
  }
</style>
</head>
<body>
<main class="canvas">

  <section class="card card--front" aria-label="Business card front">
    <div class="name-disc">
      <p class="name">Rosalind<br>Pember</p>
      <p class="role">Stylist</p>
    </div>
    <address class="contact">
      rosapember@quillnet.co.nz<br>0218846193
    </address>
  </section>

  <section class="card card--back" aria-label="Business card back">
    <div class="name-disc">
      <p class="name">Rosalind<br>Pember</p>
      <p class="role">Stylist</p>
    </div>
  </section>

</main>
</body>
</html>
```